Design profile for MuroDeck Nordhaven

I had a logo competition here recently, and was left with two logos that I could not choose between. Therefore, I create this competition where I want a complete design package or a visual identity for the company. I want you to create design elements that can be used both in print and online. (letterhead, envelopes, business card, website, facebook, etc.) I have also attached a picture of the car I have ordered. I'm happy if you can show how the design can be used on that as well.
What is important is that the logos are treated individually, and that the design you create reflects or builds up under the logo. I want the design to be recognizable and to have a connection with the logo and what we do. (take fizzo lumo as an example. if you remove the name, but keep the red color and the white line, then you will recognize which brand it is about right away)
You choose whether you want to make proposals only for one logo, or or both, but it is important that they are treated individually. The best overall package determines which logo I use.
I have also added an image that you can use as an example background if you want it in a facebook banner for example.
It is important that the design looks professional and unique. A number of designs have come in, but many of the designs are very similar and general. Here is a video of the printer if you need inspiration: https://clipvault.example/v/Q8ZtrMx2LwK

Industry/Entity Type

WallPrinting

Requirements
Must have
• Unique an professional design that can be used both online and print
Nice to have
• Show how to use the design on a VX Tully. (see photos attached)
Should not have
• The design can be simple, but not too simple and general. I want it to give the company an identity

```html
<!DOCTYPE html>
<html lang="en">
<head>
<meta charset="utf-8">
<title>MuroDeck Nordhaven – Identity Sheet</title>
<link href="https://fonts.googleapis.com/css2?family=Roboto:wght@400;500&family=Montserrat:ital,wght@0,400;0,500;0,700;1,600;1,800&display=swap" rel="stylesheet">
<style>
:root{
  --sheet-light:#eaeaea;
  --sheet-slate:#414f63;
  --sheet-grey:#646464;
  --brand-blue:#1f3f8f;
  --brand-blue-deep:#2b2f6e;
  --brand-yellow:#ffe500;
  --brand-magenta:#e5068c;
  --ink-dark:#12131f;
  --ink:#222;
  --banner-bg:#f8f2fb;
  --banner-red:#e30a1e;
  --banner-sky:#0d9de0;
  --banner-gold:#f2b600;
}
*{margin:0;padding:0;box-sizing:border-box}
html,body{width:933px;height:1200px;overflow:hidden}
body{position:relative;font-family:'Roboto',sans-serif;background:var(--sheet-grey)}
.band{position:absolute;left:0;width:933px}
.band--light{top:0;height:390px;background:var(--sheet-light)}
.band--slate{top:390px;height:376px;background:var(--sheet-slate)}
.band--grey{top:766px;height:434px;background:var(--sheet-grey)}
.section-title{position:absolute;width:100%;text-align:center;font-weight:500;font-size:20px}
.band--light .section-title{top:18px;color:#666}
.band--slate .section-title{top:20px;color:#fff}
.band--grey .section-title{top:14px;color:#fff}
.side-label{position:absolute;width:432px;text-align:center;font-size:20px;font-weight:500}
.band--light .side-label{top:332px;color:#666}
.band--slate .side-label{top:336px;color:#fff}
.card{position:absolute;width:432px;height:247px;overflow:hidden;box-shadow:3px 4px 8px rgba(0,0,0,.35)}
.card--left{left:19px}
.card--right{left:483px}
.band--light .card{top:67px}
.band--slate .card{top:73px}
.brand-name{font-family:'Montserrat',sans-serif;font-weight:700;text-align:center;line-height:1.05}

/* card one front */
.c1-front{background:linear-gradient(135deg,var(--brand-blue),var(--brand-blue-deep))}
.c1-front .bird{position:absolute;left:130px;top:10px;width:280px;height:230px;border-radius:50%;background:radial-gradient(ellipse,rgba(90,110,200,.35),rgba(40,60,150,0) 70%)}
.c1-front .brand-name{position:absolute;left:0;top:100px;width:100%;color:#fff;font-size:24px}
.c1-front .brand-name span{display:block;font-size:10px;letter-spacing:1px}

/* card one back */
.c1-back{background:#fff}
.c1-back .strip{position:absolute;left:0;top:0;width:47px;height:100%;background:var(--brand-blue)}
.c1-back .strip-yellow{position:absolute;left:0;top:207px;width:47px;height:25px;background:var(--brand-yellow)}
.c1-back .bar-yellow{position:absolute;left:179px;top:207px;right:0;height:25px;background:var(--brand-yellow)}
.c1-back .bird{position:absolute;left:150px;top:0;width:282px;height:247px;background:radial-gradient(ellipse at 60% 50%,rgba(215,212,232,.8),rgba(245,236,205,.5) 40%,rgba(255,255,255,0) 70%)}
.c1-back .brand-name{position:absolute;right:14px;top:28px;color:#111;font-size:20px}
.c1-back .brand-name span{display:block;font-size:8px;letter-spacing:.5px}
.contact-list{position:absolute;list-style:none}
.contact-list li{position:absolute;left:0;display:flex;align-items:center;white-space:nowrap}
.c1-back .contact-list{left:20px;top:0}
.c1-back .contact-list li{font-size:9.6px;color:#333;line-height:1.3}
.c1-back .icon{width:20px;height:20px;border-radius:50%;background:var(--brand-yellow);display:flex;align-items:center;justify-content:center;margin-right:16px}
.c1-back .icon svg{width:11px;height:11px;fill:none;stroke:#1b2a5a;stroke-width:2}
.c1-back .tagline{position:absolute;left:56px;top:203px}
.tagline strong{display:block;font-weight:500;font-size:16.5px;line-height:1}
.tagline small{display:block;font-weight:500;font-size:7.6px;letter-spacing:1.6px;margin-top:4px}

/* card two front */
.c2-front{background:var(--ink-dark)}
.c2-front .wing{position:absolute;top:39px;width:20px;height:170px;background:var(--brand-magenta)}
.c2-front .wing--l{left:0;clip-path:polygon(0 12%,100% 0,100% 100%,0 88%)}
.c2-front .wing--r{right:0;clip-path:polygon(0 0,100% 12%,100% 88%,0 100%)}
.c2-front .brand-name{position:absolute;left:0;top:105px;width:100%;color:#fff;font-size:28px}
.c2-front .brand-name span{display:block;font-size:9px;letter-spacing:7px;margin-top:4px}

/* card two back */
.c2-back{background:#fff}
.c2-back .pixel-field{position:absolute;left:0;top:0;width:109px;height:100%;background:linear-gradient(90deg,#f5a0c8 0,#ffc400 18%,#e5068c 38%,#8e1b3e 58%,#2d3a8c 80%,rgba(255,255,255,0) 100%)}
.c2-back .tagline{position:absolute;left:229px;top:30px;color:var(--brand-magenta)}
.c2-back .tagline strong{font-size:17px}
.c2-back .tagline small{color:#222;font-size:8px}
.c2-back .pink-bar{position:absolute;left:352px;right:0;top:31px;height:24px;background:var(--brand-magenta)}
.c2-back .rule{position:absolute;left:229px;right:0;top:69px;height:2px;background:#111}
.c2-back .contact-list{left:228px;top:0}
.c2-back .contact-list li{font-size:8.8px;color:#444;line-height:1.3}
.c2-back .icon{width:19px;height:19px;border-radius:50%;border:1px solid #777;display:flex;align-items:center;justify-content:center;margin-right:9px}
.c2-back .icon svg{width:10px;height:10px;fill:none;stroke:var(--brand-magenta);stroke-width:2}

/* banner */
.banner{position:absolute;left:47px;top:63px;width:838px;height:310px;background:var(--banner-bg);overflow:hidden}
.banner svg.shapes{position:absolute;left:0;top:0}
.banner .photo{position:absolute;left:0;top:0;width:838px;height:310px;clip-path:polygon(535px 0,838px 0,838px 310px,549px 310px,403px 147px);background:linear-gradient(120deg,#d9d4c6 0%,#b9a98a 35%,#6a6350 60%,#3d4a3a 100%)}
.banner .brand-name{position:absolute;left:12px;top:28px;color:#fff;font-size:17px;text-align:left}
.banner .brand-name span{display:block;font-size:7px;letter-spacing:.5px;font-weight:700}
.banner-copy{position:absolute;left:122px;top:96px;font-family:'Montserrat',sans-serif}
.banner-copy h1{font-style:italic;font-weight:800;font-size:22.5px;color:var(--banner-red);letter-spacing:-.5px;line-height:1}
.banner-copy h2{font-style:italic;font-weight:600;font-size:18px;color:#555;margin-top:5px;line-height:1}
.banner-copy .rule{width:64px;height:2px;background:var(--banner-gold);margin-top:13px}
.banner-copy p{font-size:12.4px;color:#888;line-height:1.4;margin-top:9px;width:240px}
.btn-join{position:absolute;left:122px;top:242px;width:54px;height:15px;border-radius:2px;background:var(--banner-gold);color:#fff;font:700 7.5px 'Montserrat',sans-serif;display:flex;align-items:center;justify-content:center}
.banner-foot{position:absolute;left:122px;top:268px;display:flex;align-items:center;font-family:'Montserrat',sans-serif;font-size:9.5px;color:#555;letter-spacing:1px}
.banner-foot .social{display:flex;gap:4px;margin:0 8px 0 44px}
.banner-foot .social i{width:12px;height:12px;border-radius:50%;background:var(--banner-gold);display:block}
</style>
</head>
<body>

<section class="band band--light">
  <h2 class="section-title">Visiting card</h2>

  <div class="card card--left c1-front">
    <div class="bird" role="img" aria-label="Faint hummingbird illustration in blue tones"></div>
    <div class="brand-name">MuroDeck<span>NORDHAVEN</span></div>
  </div>

  <div class="card card--right c1-back">
    <div class="bird" role="img" aria-label="Soft watercolour hummingbird illustration"></div>
    <div class="strip"></div>
    <div class="strip-yellow"></div>
    <div class="bar-yellow"></div>
    <div class="brand-name">MuroDeck<span>NORDHAVEN</span></div>
    <ul class="contact-list">
      <li style="top:75px"><span class="icon"><svg viewBox="0 0 12 12"><path d="M6 11C3 7 2.5 5.5 2.5 4.5a3.5 3.5 0 0 1 7 0C9.5 5.5 9 7 6 11z"/><circle cx="6" cy="4.5" r="1.2"/></svg></span><span>436 your street name<br>Your City Name, Country 123</span></li>
      <li style="top:105px"><span class="icon"><svg viewBox="0 0 12 12"><path d="M3 1.5l2 2-1 1.2a6 6 0 0 0 3.3 3.3l1.2-1 2 2-1.3 1.5C5.5 10.5 1.5 6.5 1.5 2.8z"/></svg></span><span>123 456 7890</span></li>
      <li style="top:132px"><span class="icon"><svg viewBox="0 0 12 12"><rect x="1.5" y="3" width="9" height="6"/><path d="M1.5 3L6 6.5 10.5 3"/></svg></span><span>info@murodecknordhaven.com</span></li>
      <li style="top:160px"><span class="icon"><svg viewBox="0 0 12 12"><circle cx="6" cy="6" r="4.5"/><path d="M1.5 6h9M6 1.5c-2 2.5-2 6.5 0 9M6 1.5c2 2.5 2 6.5 0 9"/></svg></span><span>www.murodecknordhaven.com</span></li>
    </ul>
    <div class="tagline"><strong>LOREM IPSUM</strong><small>PRINTING &amp; GRAPHICS</small></div>
  </div>

  <div class="side-label" style="left:19px">Front</div>
  <div class="side-label" style="left:483px">Back</div>
</section>

<section class="band band--slate">
  <h2 class="section-title">Visiting card</h2>

  <div class="card card--left c2-front">
    <div class="wing wing--l"></div>
    <div class="wing wing--r"></div>
    <div class="brand-name">MuroDeck<span>NORDHAVEN</span></div>
  </div>

  <div class="card card--right c2-back">
    <div class="pixel-field" role="img" aria-label="Decorative pattern of colourful pixel bars in pink, yellow, cyan and navy"></div>
    <div class="tagline"><strong>LOREM IPSUM</strong><small>PRINTING &amp; GRAPHICS</small></div>
    <div class="pink-bar"></div>
    <div class="rule"></div>
    <ul class="contact-list">
      <li style="top:126px"><span class="icon"><svg viewBox="0 0 12 12"><path d="M6 11C3 7 2.5 5.5 2.5 4.5a3.5 3.5 0 0 1 7 0C9.5 5.5 9 7 6 11z"/><circle cx="6" cy="4.5" r="1.2"/></svg></span><span>436 your street name<br>Your City Name, Country 123</span></li>
      <li style="top:153px"><span class="icon"><svg viewBox="0 0 12 12"><path d="M3 1.5l2 2-1 1.2a6 6 0 0 0 3.3 3.3l1.2-1 2 2-1.3 1.5C5.5 10.5 1.5 6.5 1.5 2.8z"/></svg></span><span>123 456 7890</span></li>
      <li style="top:178px"><span class="icon"><svg viewBox="0 0 12 12"><rect x="1.5" y="3" width="9" height="6"/><path d="M1.5 3L6 6.5 10.5 3"/></svg></span><span>info@murodecknordhaven.com</span></li>
      <li style="top:204px"><span class="icon"><svg viewBox="0 0 12 12"><circle cx="6" cy="6" r="4.5"/><path d="M1.5 6h9M6 1.5c-2 2.5-2 6.5 0 9M6 1.5c2 2.5 2 6.5 0 9"/></svg></span><span>www.murodecknordhaven.com</span></li>
    </ul>
  </div>

  <div class="side-label" style="left:19px">Front</div>
  <div class="side-label" style="left:483px">Back</div>
</section>

<section class="band band--grey">
  <h2 class="section-title">Website Banner</h2>

  <div class="banner">
    <div class="photo" role="img" aria-label="Photo of a print technician working at a large-format printing machine"></div>
    <svg class="shapes" width="838" height="310" viewBox="0 0 838 310">
      <polygon points="0,0 216,0 0,214" fill="#d6d6d6"/>
      <polygon points="0,0 208,0 0,203" fill="#050505"/>
      <polygon points="494,0 594,0 494,98" fill="var(--banner-sky)"/>
      <polygon points="485,197 543,256 462,277" fill="var(--banner-red)"/>
      <polygon points="499,272 543,262 530,306" fill="var(--banner-sky)"/>
      <polygon points="808,110 808,310 700,310" fill="var(--brand-yellow)" opacity=".55"/>
    </svg>
    <div class="brand-name">MuroDeck<span>NORDHAVEN</span></div>
    <div class="banner-copy">
      <h1>PRINT MEDIA COMPANY</h1>
      <h2>PRINT &amp; GRAPHICS</h2>
      <div class="rule"></div>
      <p>Lorem ipsum dolor sit amet, consecte-tur adipiscing elit, sed do eiusmod</p>
    </div>
    <div class="btn-join">JOIN US</div>
    <div class="banner-foot">
      <span>www.websitename.com</span>
      <span class="social"><i></i><i></i><i></i><i></i></span>
      <span>/ brandname</span>
    </div>
  </div>
</section>

</body>
</html>
```